Irrigation Business needs their business cards modernised and revamped

I would like to keep my current logo, colours and revamp the format of the card.

I would like the card to be clean yet important.

Im not sure if you include texture but i would like the named logo to be indented into the card etc.

show me something alive and free something thats clinical to the point yet has a feel of achievement. i would like people to go nice card.

Target Market(s)

high end clients, corporate, sports field manger, the guys that make the decisions

Industry/Entity Type

Business

Contact Information for Business Card

nformation to be included

Dorian Hesk (Director)
0487253916
dorian@tfcraft.biz
www.taddsfieldcrafts.com

instagram logo
google logo
facebook logo

Colors

Designer to choose colors to be used in the design.

Requirements
Nice to have
• indentations a really nice feel to the card good texture

```html
<!DOCTYPE html>
<html lang="en">
<head>
<meta charset="utf-8">
<title>Tadd's Field Crafts – Business Card</title>
<link href="https://fonts.googleapis.com/css2?family=Roboto+Condensed:wght@400;700&family=Open+Sans:wght@400;600&display=swap" rel="stylesheet">
<style>
  :root {
    --stage: #2a2a2a;
    --paper: #f2f2f2;
    --brand-blue: #2f63a8;
    --sky-blue: #2fa1d6;
    --field-green: #27a05a;
    --white: #ffffff;
  }
  * { margin: 0; padding: 0; box-sizing: border-box; }
  html, body { width: 1200px; height: 960px; overflow: hidden; }
  body {
    background: var(--stage);
    position: relative;
    font-family: "Open Sans", Arial, sans-serif;
  }
  .card {
    position: absolute;
    width: 600px;
    height: 343px;
    overflow: hidden;
  }
  .card--front { left: 314px; top: 113px; background: var(--paper); }
  .card--back { left: 311px; top: 472px; background: var(--field-green); }

  .wave { position: absolute; inset: 0; width: 600px; height: 343px; }

  .brand {
    position: absolute;
    left: 40px;
    top: 40px;
    width: 230px;
    text-align: center;
  }
  .brand__dot {
    width: 76px; height: 76px;
    border-radius: 50%;
    background: var(--brand-blue);
    margin: 0 auto 12px;
  }
  .brand__name {
    font-family: "Roboto Condensed", Arial, sans-serif;
    font-weight: 700;
    font-size: 25px;
    color: var(--brand-blue);
    letter-spacing: 0.3px;
    white-space: nowrap;
  }

  .contact {
    position: absolute;
    right: 28px;
    top: 204px;
    text-align: right;
    color: var(--white);
  }
  .contact__name {
    font-family: "Roboto Condensed", Arial, sans-serif;
    font-weight: 700;
    font-size: 21px;
    line-height: 24px;
  }
  .contact__role {
    font-family: "Roboto Condensed", Arial, sans-serif;
    font-weight: 700;
    font-size: 15px;
    line-height: 20px;
    margin-bottom: 10px;
  }
  .contact__line {
    font-size: 14px;
    line-height: 19.5px;
    display: flex;
    justify-content: flex-end;
    align-items: center;
    gap: 7px;
  }
  .contact__line svg { width: 13px; height: 13px; fill: var(--white); }

  .social {
    position: absolute;
    left: 25px;
    top: 298px;
    display: flex;
    gap: 4px;
  }
  .social__item {
    width: 25px; height: 25px;
    border-radius: 50%;
    background: var(--white);
  }

  .back__brand {
    position: absolute;
    left: 0; right: 0;
    top: 148px;
    text-align: center;
    color: var(--paper);
    font-family: "Roboto Condensed", Arial, sans-serif;
    font-weight: 700;
  }
  .back__brand-main { font-size: 48px; line-height: 52px; letter-spacing: -0.5px; }
  .back__brand-sub { font-size: 30px; line-height: 36px; letter-spacing: 9px; margin-left: 9px; }
  .back__url {
    position: absolute;
    left: 0; right: 0;
    top: 284px;
    text-align: center;
    color: rgba(255,255,255,0.9);
    font-size: 15px;
    letter-spacing: 2.2px;
  }
</style>
</head>
<body>

<section class="card card--front">
  <svg class="wave" viewBox="0 0 600 343" aria-hidden="true">
    <path d="M0,166 C50,268 130,284 230,271 C360,254 470,128 600,50 L600,343 L0,343Z" fill="var(--sky-blue)"/>
    <path d="M0,172 C50,274 130,290 230,277 C360,260 470,148 600,72 L600,343 L0,343Z" fill="var(--white)"/>
    <path d="M0,176 C50,278 130,294 230,281 C360,264 470,152 600,76 L600,343 L0,343Z" fill="var(--field-green)"/>
    <path d="M0,186 C45,284 140,292 240,284 C365,270 470,153 600,76 L600,343 L0,343Z" fill="var(--brand-blue)"/>
  </svg>

  <div class="brand">
    <div class="brand__dot"></div>
    <div class="brand__name">TADD'S FIELD CRAFTS</div>
  </div>

  <div class="contact">
    <div class="contact__name">DORIAN HESK</div>
    <div class="contact__role">DIRECTOR</div>
    <div class="contact__line">0487253916
      <svg viewBox="0 0 24 24"><path d="M6.6 10.8a15.1 15.1 0 0 0 6.6 6.6l2.2-2.2c.3-.3.7-.4 1-.2 1.1.4 2.3.6 3.6.6.6 0 1 .4 1 1V20c0 .6-.4 1-1 1A17 17 0 0 1 3 4c0-.6.4-1 1-1h3.5c.6 0 1 .4 1 1 0 1.3.2 2.5.6 3.6.1.3 0 .7-.2 1z"/></svg>
    </div>
    <div class="contact__line">dorian@tfcraft.biz
      <svg viewBox="0 0 24 24"><path d="M2 5h20v14H2z M2 5l10 8 10-8" fill="var(--white)"/><path d="M3 6l9 7 9-7" fill="none" stroke="var(--brand-blue)" stroke-width="1.8"/></svg>
    </div>
    <div class="contact__line">taddsfieldcrafts.com
      <svg viewBox="0 0 24 24"><circle cx="12" cy="12" r="10"/><path d="M7 8c2 0 3 1 3 3s-2 2-2 4M15 5c-1 2 0 3 2 3s2 3 1 5" fill="none" stroke="var(--brand-blue)" stroke-width="1.8"/></svg>
    </div>
  </div>

  <div class="social" aria-label="Social profiles">
    <span class="social__item"></span>
    <span class="social__item"></span>
    <span class="social__item"></span>
  </div>
</section>

<section class="card card--back">
  <div class="back__brand">
    <div class="back__brand-main">TADD'S FIELD</div>
    <div class="back__brand-sub">CRAFTS</div>
  </div>
  <div class="back__url">www.taddsfieldcrafts.com</div>
</section>

</body>
</html>
```